A Dedicated Thank You to my Dad

Proposed Dimensions: Approx. 20" x 30"

For Father's Day, I wrote a dedication to my Dad that encapsulates my gratitude for everything he does, and everything he is. His birthday is on August 3, but it is more important for me to transform this dedication into a meaningful and memorable gift than to meet any deadline. I would love an image that captures the relationship between a father and his son, accompanied by my words of thanks in some sort of font that is appropriate for the message (calligprahy? not sure about that).

I had actually posted the Thank You on Pixelmarrow as a public post, so anyone with an account can read it: https://www.pixelmarrow.example/photo.php?fbid=40872219360548813&set=a.318760942157.6650129.3908471&type=1&theater

Only the words starting with "Thank you ..." should be on the poster.

Target Market(s)

This is a personal gift for my Dad. He doesn't have the best of eyesight, so having the words in a really small font would not be particularly helpful. :-)

Requirements
Must have
• * Personable
* Warm
* Inviting
* Memorable
* Understated more favored over Loud
Should not have
• * An entire palette of colors
* Wacky colors or fonts

```html
<!DOCTYPE html>
<html lang="en">
<head>
<meta charset="UTF-8">
<title>A Dedicated Thank You to my Dad</title>
<link href="https://fonts.googleapis.com/css2?family=Dancing+Script:wght@500&family=Didact+Gothic&display=swap" rel="stylesheet">
<style>
  :root {
    --sky-cream: #ece4bf;
    --sky-teal: #c3d2c4;
    --cloud: #f4efd8;
    --horizon: #e3dcb0;
    --grass-light: #c2bd72;
    --grass-mid: #9fa357;
    --grass-deep: #7f8a47;
    --script-ink: #ffffff;
    --script-shadow: rgba(60, 55, 40, 0.55);
    --body-ink: rgba(20, 18, 14, 0.88);
  }
  html, body {
    margin: 0;
    padding: 0;
    width: 800px;
    height: 1200px;
    overflow: hidden;
    background: var(--sky-cream);
  }
  .poster {
    position: relative;
    width: 800px;
    height: 1200px;
    overflow: hidden;
  }
  .poster__scene {
    position: absolute;
    inset: 0;
    background:
      radial-gradient(ellipse 420px 200px at 640px 430px, var(--cloud) 0%, rgba(244,239,216,0) 70%),
      radial-gradient(ellipse 360px 140px at 120px 180px, rgba(244,239,216,0.7) 0%, rgba(244,239,216,0) 70%),
      linear-gradient(180deg,
        var(--sky-cream) 0%,
        var(--sky-teal) 22%,
        var(--sky-teal) 38%,
        var(--horizon) 62%,
        var(--grass-light) 72%,
        var(--grass-mid) 86%,
        var(--grass-deep) 100%);
  }
  .dedication {
    position: absolute;
    left: 0;
    right: 0;
    margin: 0;
    text-align: center;
  }
  .dedication--welcome {
    top: 120px;
    font-family: 'Dancing Script', cursive;
    font-weight: 500;
    font-size: 50px;
    line-height: 112px;
    color: var(--script-ink);
    text-shadow: 2px 4px 6px var(--script-shadow);
  }
  .dedication--carry {
    top: 712px;
    font-family: 'Didact Gothic', sans-serif;
    font-size: 39px;
    line-height: 62px;
    color: var(--body-ink);
  }
</style>
</head>
<body>
  <main class="poster">
    <div class="poster__scene" role="img" aria-label="Faded vintage photograph of a father walking hand in hand with his young son across a grassy hill under a pale sky, seen from behind"></div>
    <p class="dedication dedication--welcome">Thank you for welcoming<br>more people to stay with us<br>than I can count.</p>
    <p class="dedication dedication--carry">Thank you for always carrying us<br>to the car after we fell asleep,<br>even after we were definitely<br>old enough to walk it.</p>
  </main>
</body>
</html>
```